Bright Path Mentors Needs A New Website Design

We need a 8 page website designed for "Bright Path Mentors .ca" similar in design to: "quill ridge learning .com".

The winner/successful candidate on the home page will be asked to complete the following inner pages to complete the project:

About Us
Philosophy
How We Work
Work With Us
Blog
Find A Tutor
Contact

Target Market(s)

Tutoring business clients/children

Industry/Entity Type

Education

Number of Pages Required

5+ page

Font styles to use
Sans Serif

Requirements
Must have
• The attached logo included of course. Similar design to the design provided above in the brief. Clear high quality high resolution images of children in school settings.

```html
<!DOCTYPE html>
<html lang="en">
<head>
<meta charset="utf-8">
<title>Bright Path Mentors</title>
<link href="https://fonts.googleapis.com/css2?family=Montserrat:wght@400;600;700&family=Open+Sans:wght@400;600;700&family=Raleway:wght@300;400&display=swap" rel="stylesheet">
<style>
:root{
  --orange:#f7941d;
  --navy:#2b3990;
  --navy-deep:#262f86;
  --ink:#333333;
  --muted:#8a8a8a;
  --soft:#f1f1f1;
  --line:#d9d9d9;
  --white:#ffffff;
}
*{box-sizing:border-box;margin:0;padding:0}
html,body{width:1200px;height:4050px;overflow:hidden}
body{font-family:"Open Sans",sans-serif;color:var(--ink);background:var(--white);position:relative}
section,header,nav,footer{position:relative;width:1200px;overflow:hidden}
.abs{position:absolute}
.heading{font-family:"Montserrat",sans-serif;font-weight:600;letter-spacing:.5px}
.rule{width:56px;height:2px;background:var(--orange)}
.small{font-size:12.5px;line-height:20px;color:var(--muted)}

/* header */
.site-header{height:100px;background:var(--white)}
.phone{left:110px;top:36px;display:flex;align-items:center;gap:12px;font-size:16px;font-weight:600}
.brand{left:0;right:0;top:18px;text-align:center}
.brand-mark{width:46px;height:46px;border-radius:50%;background:var(--navy);margin:0 auto 4px}
.brand-name{font-family:"Montserrat",sans-serif;font-weight:700;font-size:11px;color:var(--navy);letter-spacing:1px}
.social{right:110px;top:34px;display:flex;gap:22px}
.social span{width:26px;height:26px;border-radius:50%;background:var(--navy);display:block}
.social span.alt{background:#d93a2b}

/* nav */
.main-nav{height:43px;background:var(--orange);display:flex;justify-content:center;align-items:center;gap:42px}
.main-nav a{color:var(--white);text-decoration:none;font-family:"Montserrat",sans-serif;font-size:12px;letter-spacing:.3px}
.main-nav a.active{border-bottom:1px solid var(--white)}

/* hero */
.hero{height:464px}
.hero-photo{inset:0;background:linear-gradient(100deg,#8a95b4 0%,#b9c2d6 45%,#d7dce6 70%,#aab3c7 100%)}
.hero-title{left:110px;top:143px;font-family:"Montserrat",sans-serif;font-weight:700;font-size:31px;color:var(--white)}
.hero-rule{left:110px;top:195px;width:56px;height:2px;background:var(--white)}
.hero-text{left:110px;top:230px;width:560px;font-size:13px;line-height:20px;color:var(--white)}
.btn-outline{border:1.5px solid var(--white);color:var(--white);font-size:12px;padding:8px 22px;display:inline-block}
.hero-btn{left:110px;top:302px}
.finder{left:780px;top:80px;width:310px;height:307px;background:var(--white)}
.finder-head{height:42px;background:var(--navy);color:var(--white);font-family:"Montserrat",sans-serif;font-weight:700;font-size:15px;text-align:center;line-height:42px}
.field{margin:0 33px;height:52px;border-bottom:1px solid var(--line);font-size:11px;color:#aaa;padding-top:26px;position:relative}
.field .caret{position:absolute;right:4px;top:28px;width:7px;height:7px;border-right:1px solid #aaa;border-bottom:1px solid #aaa;transform:rotate(45deg)}
.btn-orange{background:var(--orange);color:var(--white);font-family:"Montserrat",sans-serif;font-weight:600;font-size:14px;text-align:center}
.finder .btn-orange{margin:30px 33px 0;height:42px;line-height:42px}

/* partners */
.partners{height:93px;border-bottom:1px solid var(--line)}
.partners-title{left:110px;top:35px;font-family:"Montserrat",sans-serif;font-weight:700;font-size:20px;color:var(--navy)}
.partners-title span{color:var(--orange)}
.badge{top:27px;height:40px;border-radius:6px;background:#e2e4ea}

/* about */
.about{height:510px;background:var(--soft)}
.about-photo{left:110px;top:95px;width:420px;height:310px;background:linear-gradient(135deg,#e9dccf,#c8b09a 60%,#9aa5b5);box-shadow:0 8px 18px rgba(0,0,0,.18)}
.col-title{font-family:"Montserrat",sans-serif;font-weight:600;font-size:16px}
.about-copy{left:612px;top:105px;width:470px}
.about-copy .rule{margin:16px 0 26px}
.facility{display:flex;gap:22px;margin-top:36px}
.icon-ring{width:34px;height:34px;border-radius:50%;border:2px solid var(--orange);flex:none;display:flex;align-items:center;justify-content:center}
.icon-ring i{width:14px;height:14px;background:var(--orange);border-radius:2px}
.facility b{font-size:12px;display:block;margin-bottom:6px}

/* philosophy */
.philosophy{height:510px}
.philosophy-photo{inset:0;background:linear-gradient(120deg,#c7d9ea,#f1e2cf 50%,#cfe0ee)}
.philosophy-panel{left:0;top:0;width:610px;height:510px}
.philosophy-copy{left:110px;top:125px;width:440px;color:var(--white)}
.philosophy-copy .col-title{color:var(--white)}
.philosophy-copy .rule{margin:14px 0 28px}
.philosophy-copy p{font-size:12.5px;line-height:19px;margin-bottom:18px}
.philosophy-copy .btn-orange{display:inline-block;font-size:11px;padding:10px 20px;margin-top:22px}

/* how it works */
.how{height:450px}
.timeline{left:641px;top:0;width:2px;height:450px;background:var(--orange)}
.video{left:138px;top:88px;width:387px;height:252px;background:linear-gradient(135deg,#d9c6b0,#b39a86 50%,#7f8fa8);box-shadow:0 8px 18px rgba(0,0,0,.2);border:8px solid #f4f4f4}
.play{left:50%;top:50%;width:62px;height:62px;margin:-31px 0 0 -31px;border-radius:50%;background:var(--navy)}
.how-title{left:698px;top:88px}
.step{left:612px;display:flex;gap:26px;align-items:flex-start}
.step-num{width:60px;height:60px;border-radius:50%;border:2px solid var(--orange);background:var(--white);color:var(--navy);font-family:"Montserrat",sans-serif;font-size:22px;text-align:center;line-height:56px;flex:none}
.step b{font-size:12.5px;display:block;margin:4px 0 4px}

/* blogs */
.blogs{height:520px;background:var(--orange)}
.blogs-title{left:0;right:0;top:78px;text-align:center;color:var(--white);font-size:18px}
.blogs-rule{left:572px;top:115px;background:var(--white)}
.card{top:175px;width:310px;height:275px;background:var(--white)}
.card-photo{height:175px;background:linear-gradient(120deg,#f1e3d2,#d8c0a8 50%,#a7b9cc)}
.date{left:0;top:100px;width:76px;height:75px;background:var(--navy);color:var(--white);text-align:center;font-family:"Montserrat",sans-serif}
.date b{font-size:28px;display:block;line-height:34px;padding-top:10px}
.date small{font-size:8px}
.card h3{font-family:"Montserrat",sans-serif;font-weight:600;font-size:12.5px;color:var(--orange);margin:8px 16px 6px}
.card p{font-size:11px;line-height:15px;margin:0 16px;color:#222}

/* testimonials */
.testimonials{height:475px}
.test-title{left:0;right:0;top:85px;text-align:center;font-family:"Raleway",sans-serif;font-weight:300;font-size:30px}
.test-rule{left:572px;top:138px}
.quote{top:198px;width:232px;height:110px;background:#efefef;text-align:center;font-style:italic;font-size:11px;line-height:15px;color:var(--muted);padding:18px 18px}
.person{top:330px;display:flex;align-items:center;gap:16px}
.avatar{width:60px;height:60px;border-radius:50%;background:linear-gradient(135deg,#e8d3bf,#b08e74)}
.person b{font-size:16px;font-weight:600;display:block}
.person small{font-size:11px;color:var(--muted)}

/* work with us */
.work{height:275px}
.work-photo{inset:0;background:linear-gradient(90deg,#3d4fa0,#5d6db0 40%,#7a86bd 70%,#4a5aa3)}
.work-title{left:0;right:0;top:55px;text-align:center;color:var(--white);font-size:30px}
.work-text{left:0;right:0;top:132px;text-align:center;color:var(--white);font-size:13px}
.work-btn{left:542px;top:184px;font-size:11px;padding:8px 18px}

/* contact */
.contact{height:525px}
.contact-title{left:0;right:0;top:80px;text-align:center;font-family:"Raleway",sans-serif;font-weight:400;font-size:30px}
.contact-rule{left:572px;top:130px}
.contact-sub{left:0;right:0;top:150px;text-align:center;font-size:12px;color:var(--muted)}
.input{height:40px;border-bottom:1px solid var(--line);font-size:12px;color:#aaa;padding-top:8px}
.send{left:535px;top:405px;width:130px;height:38px;line-height:38px;font-size:12px}

/* footer */
.site-footer{height:85px;background:var(--navy-deep)}
.foot-social{left:0;right:0;top:20px;display:flex;justify-content:center;gap:26px}
.foot-social span{width:18px;height:18px;border-radius:50%;background:var(--white);display:block}
.copyright{left:0;right:0;top:56px;text-align:center;font-size:10px;color:#bfc3e6}
</style>
</head>
<body>

<header class="site-header">
  <div class="abs phone">
    <svg width="24" height="24" viewBox="0 0 24 24"><circle cx="12" cy="12" r="11" fill="none" stroke="#2b3990" stroke-width="1.6"/><path d="M8.5 6.5l2 2-1.2 1.6c.8 1.6 2 2.8 3.6 3.6l1.6-1.2 2 2-1.4 1.8c-3.9-.4-7.9-4.4-8.3-8.3z" fill="#2b3990"/></svg>
    012 5550 417
  </div>
  <div class="abs brand">
    <div class="brand-mark"></div>
    <div class="brand-name">BRIGHT PATH MENTORS</div>
  </div>
  <div class="abs social"><span></span><span></span><span class="alt"></span><span></span></div>
</header>

<nav class="main-nav">
  <a href="#" class="active">ABOUT US</a><a href="#">PHILOSOPHY</a><a href="#">HOW WE WORK</a><a href="#" class="active">WORK WITH US</a><a href="#">BLOG</a><a href="#">FIND A TUTOR</a><a href="#">CONTACT</a>
</nav>

<section class="hero">
  <div class="abs hero-photo" role="img" aria-label="Tutor helping a student at a desk with a laptop"></div>
  <h1 class="abs hero-title">THE EASIEST WAY TO FIND TUTORS</h1>
  <div class="abs hero-rule"></div>
  <p class="abs hero-text">Lorem ipsum dolor sit amet, consectetur adipiscing elit. Aenean euismod bibendum laoreet. Proin gravida dolor sit amet lacus accumsan et viverra justo commodo.</p>
  <a class="abs btn-outline hero-btn">More Info</a>
  <form class="abs finder">
    <div class="finder-head">FIND A TUTOR</div>
    <div class="field">Subject</div>
    <div class="field">Location</div>
    <div class="field">Price Range<span class="caret"></span></div>
    <div class="btn-orange">FIND</div>
  </form>
</section>

<section class="partners">
  <div class="abs partners-title">OUR <span>PARTNERS</span></div>
  <div class="abs badge" style="left:310px;width:155px"></div>
  <div class="abs badge" style="left:500px;width:255px"></div>
  <div class="abs badge" style="left:790px;width:70px"></div>
  <div class="abs badge" style="left:888px;width:160px"></div>
</section>

<section class="about">
  <div class="abs about-photo" role="img" aria-label="Mother and son reading together at a table"></div>
  <div class="abs about-copy">
    <h2 class="col-title">ABOUT US</h2>
    <div class="rule"></div>
    <p class="small">Lorem ipsum dolor sit amet, consectetur adipiscing elit. Aenean euismod bibendum laoreet. Proin gravida dolor sit amet lacus accumsan et viverra justo commodo.</p>
    <div class="facility"><div class="icon-ring"><i></i></div><div><b>Facility One</b><p class="small">Lorem ipsum dolor sit amet, consectetur adipiscing elit. Aenean euismod bibendum laoreet.</p></div></div>
    <div class="facility"><div class="icon-ring"><i></i></div><div><b>Facility Two</b><p class="small">Lorem ipsum dolor sit amet, consectetur adipiscing elit. Aenean euismod bibendum laoreet. Proin gravida dolor sit amet lacus accumsan et viverra justo commodo.</p></div></div>
  </div>
</section>

<section class="philosophy">
  <div class="abs philosophy-photo" role="img" aria-label="Smiling mother and son working on a laptop"></div>
  <svg class="abs philosophy-panel" viewBox="0 0 610 510" aria-hidden="true">
    <polygon points="0,0 578,0 610,510 0,510" fill="#f7941d"/>
    <polygon points="0,0 566,0 596,510 0,510" fill="#2b3990"/>
  </svg>
  <div class="abs philosophy-copy">
    <h2 class="col-title">PHILOSOPHY</h2>
    <div class="rule"></div>
    <p>Lorem ipsum dolor sit amet, consectetur adipiscing elit. Aenean euismod bibendum laoreet. Proin gravida dolor sit amet lacus accumsan et viverra justo commodo. Proin sodales pulvinar tempor. Cum sociis natoque penatibus et magnis dis parturient montes.</p>
    <p>Lorem ipsum dolor sit amet, consectetur adipiscing elit. Aenean euismod bibendum laoreet.</p>
    <a class="btn-orange">READ MORE</a>
  </div>
</section>

<section class="how">
  <div class="abs timeline"></div>
  <div class="abs video" role="img" aria-label="Video still of a tutor and child writing together">
    <svg class="abs play" viewBox="0 0 62 62"><circle cx="31" cy="31" r="29" fill="#fff" stroke="#2b3990" stroke-width="4"/><polygon points="25,19 44,31 25,43" fill="#2b3990"/></svg>
  </div>
  <h2 class="abs col-title how-title">HOW IT WORKS</h2>
  <div class="abs step" style="top:150px"><div class="step-num">1</div><div><b>Step One</b><p class="small" style="width:360px">Lorem ipsum dolor sit amet, consectetur adipiscing elit. Aenean euismod bibendum laoreet.</p></div></div>
  <div class="abs step" style="top:228px"><div class="step-num">2</div><div><b>Step Two</b><p class="small" style="width:360px">Lorem ipsum dolor sit amet, consectetur adipiscing elit. Aenean euismod bibendum laoreet.</p></div></div>
  <div class="abs step" style="top:306px"><div class="step-num">3</div><div><b>Step Three</b><p class="small" style="width:360px">Lorem ipsum dolor sit amet, consectetur adipiscing elit. Aenean euismod bibendum laoreet.</p></div></div>
</section>

<section class="blogs">
  <h2 class="abs heading blogs-title">OUR BLOGS</h2>
  <div class="abs rule blogs-rule"></div>
  <article class="abs card" style="left:110px">
    <div class="card-photo abs" style="position:relative" role="img" aria-label="Parent and child studying with pencils"><div class="abs date"><b>04</b><small>SEP 16</small></div></div>
    <h3>LOREM IPSUM IS SIMPLY DUMMY TEXT</h3>
    <p>simply dummy text of the printing and typesetting industry. Lorem Ipsum has been the industry's standard dummy text ever</p>
  </article>
  <article class="abs card" style="left:445px">
    <div class="card-photo abs" style="position:relative" role="img" aria-label="Parent and child studying with pencils"><div class="abs date"><b>04</b><small>SEP 16</small></div></div>
    <h3>LOREM IPSUM IS SIMPLY DUMMY TEXT</h3>
    <p>simply dummy text of the printing and typesetting industry. Lorem Ipsum has been the industry's standard dummy text ever</p>
  </article>
  <article class="abs card" style="left:780px">
    <div class="card-photo abs" style="position:relative" role="img" aria-label="Parent and child studying with pencils"><div class="abs date"><b>04</b><small>SEP 16</small></div></div>
    <h3>LOREM IPSUM IS SIMPLY DUMMY TEXT</h3>
    <p>simply dummy text of the printing and typesetting industry. Lorem Ipsum has been the industry's standard dummy text ever</p>
  </article>
</section>

<section class="testimonials">
  <h2 class="abs test-title">WHAT OUR CUSTOMERS ARE SAYING</h2>
  <div class="abs rule test-rule"></div>
  <blockquote class="abs quote" style="left:148px">Lorem ipsum dolor sit amet, consectetur adipiscing elit. Doloribus accusamus expedita repellat similique odio aspernatur ex, architecto eaque</blockquote>
  <blockquote class="abs quote" style="left:483px">Lorem ipsum dolor sit amet, consectetur adipiscing elit. Doloribus accusamus expedita repellat similique odio aspernatur ex, architecto eaque</blockquote>
  <blockquote class="abs quote" style="left:820px">Lorem ipsum dolor sit amet, consectetur adipiscing elit. Doloribus accusamus expedita repellat similique odio aspernatur ex, architecto eaque</blockquote>
  <div class="abs person" style="left:148px"><div class="avatar" role="img" aria-label="Portrait of Nadia R."></div><div><b>Nadia R.</b><small>Elementary Student</small></div></div>
  <div class="abs person" style="left:483px"><div class="avatar" role="img" aria-label="Portrait of Owen T."></div><div><b>Owen T.</b><small>University Student</small></div></div>
  <div class="abs person" style="left:820px"><div class="avatar" role="img" aria-label="Portrait of Clara M."></div><div><b>Clara M.</b><small>Primary School Student</small></div></div>
</section>

<section class="work">
  <div class="abs work-photo" role="img" aria-label="Group of smiling students in a classroom"></div>
  <h2 class="abs heading work-title">WORK WITH US</h2>
  <p class="abs work-text">Interested to work with us? We open recruitment for tutor. Apply for the job now!</p>
  <a class="abs btn-outline work-btn">MORE INFO</a>
</section>

<section class="contact">
  <h2 class="abs contact-title">CONTACT US</h2>
  <div class="abs rule contact-rule"></div>
  <p class="abs contact-sub">Have questions? Don't hesitate to drop us message</p>
  <div class="abs" style="left:125px;top:220px;width:440px">
    <div class="input">Name</div>
    <div class="input" style="margin-top:12px">Email</div>
    <div class="input" style="margin-top:12px">Subject</div>
  </div>
  <div class="abs" style="left:640px;top:220px;width:440px">
    <div class="input" style="height:144px">Message</div>
  </div>
  <div class="abs btn-orange send">Send Message</div>
</section>

<footer class="site-footer">
  <div class="abs foot-social"><span></span><span></span><span></span><span></span></div>
  <p class="abs copyright">© 2016 by Bright Path Mentors</p>
</footer>

</body>
</html>
```